Business card design needed

Our modern electrical contracting company requires business card design utilising our logo and incorporating our tag line "Service when you need it". We specialise in assisting our customers 24/7 offering a breakdown service.

Industry/Entity Type

Electrical

Contact Information for Business Card

Marcus Penhale, Electrical contractor,Tel: (08) 8456 3071, Fax: (08) 8679 4315, Mob 0438 562 740, Email: marcus.penhale@brightwirepower.com.au, Web: www.brightwirepower.com.au

Requirements
Must have
• we require a 2 sided card.
Front- Logo, tag line and contact information.
Rear- service when you need it! Call now for our 24/7 breakdown service

```html
<!DOCTYPE html>
<html lang="en">
<head>
<meta charset="utf-8">
<title>Brightwire Power Business Card</title>
<link href="https://fonts.googleapis.com/css2?family=Exo+2:wght@400;600;700;800&display=swap" rel="stylesheet">
<style>
  :root {
    --page-bg: #e4e6e9;
    --card-white: #ffffff;
    --panel-dark-top: #5a5b5e;
    --panel-dark-mid: #2a2b2d;
    --panel-dark-bottom: #0e0e0f;
    --band-blue: #1f55c4;
    --band-blue-light: #6f9ef0;
    --band-blue-deep: #0f3596;
    --brand-blue: #1a4fc0;
    --text-light: #ffffff;
    --text-soft: #e6e6e6;
    --icon-dark: #2a2b2d;
  }
  * { box-sizing: border-box; margin: 0; padding: 0; }
  html, body {
    width: 1200px; height: 861px; overflow: hidden;
    background: var(--page-bg);
    font-family: "Exo 2", "Segoe UI", sans-serif;
  }
  .canvas {
    position: relative; width: 1200px; height: 861px;
    display: flex; justify-content: center; align-items: center; gap: 60px;
  }
  .card {
    position: relative; width: 330px; height: 540px;
    background: var(--card-white);
    box-shadow: 0 10px 30px rgba(0,0,0,0.25);
    overflow: hidden;
  }
  .card-shape { position: absolute; inset: 0; width: 330px; height: 540px; }
  .card-content { position: absolute; inset: 0; color: var(--text-light); text-align: center; }

  /* Rear */
  .promo { padding-top: 62px; }
  .promo-tagline { font-size: 27px; font-weight: 700; line-height: 1.28; letter-spacing: 0.5px; }
  .promo-call { margin-top: 14px; font-size: 24px; font-weight: 700; letter-spacing: 0.5px; }
  .promo-hours { font-size: 72px; font-weight: 700; line-height: 1; margin-top: 4px; }
  .promo-service { margin-top: 8px; font-size: 23px; font-weight: 700; line-height: 1.3; letter-spacing: 1px; }

  /* Front */
  .contact { padding-top: 50px; }
  .contact-name { font-size: 35px; font-weight: 600; letter-spacing: 0.5px; line-height: 1.1; }
  .contact-role { font-size: 18px; font-weight: 400; color: var(--text-soft); margin-top: 4px; letter-spacing: 0.5px; }
  .contact-list { list-style: none; text-align: left; margin: 22px 0 0 20px; }
  .contact-item { display: flex; align-items: center; gap: 8px; height: 26.5px; font-size: 14.5px; color: var(--text-soft); }
  .contact-item.small { font-size: 13px; }
  .contact-icon { width: 19px; height: 19px; flex: none; }
  .contact-tagline { margin-top: 18px; font-size: 21px; font-weight: 700; line-height: 1.2; letter-spacing: 0.5px; }

  /* Brand lockup */
  .brand {
    position: absolute; left: 0; right: 0; top: 440px;
    display: flex; justify-content: center; align-items: center; gap: 10px;
  }
  .brand-dot { width: 34px; height: 34px; border-radius: 50%; background: var(--brand-blue); flex: none; }
  .brand-name { font-size: 27px; font-weight: 800; color: var(--brand-blue); letter-spacing: 0.5px; }
</style>
</head>
<body>
<main class="canvas">

  <!-- Rear side -->
  <section class="card card-rear">
    <svg class="card-shape" viewBox="0 0 330 540" aria-hidden="true">
      <defs>
        <linearGradient id="rearDark" x1="0" y1="0" x2="0" y2="1">
          <stop offset="0" stop-color="var(--panel-dark-top)"/>
          <stop offset="0.35" stop-color="var(--panel-dark-mid)"/>
          <stop offset="1" stop-color="var(--panel-dark-bottom)"/>
        </linearGradient>
        <linearGradient id="rearBlue" x1="0" y1="0" x2="1" y2="0">
          <stop offset="0" stop-color="var(--band-blue-deep)"/>
          <stop offset="0.5" stop-color="var(--band-blue-light)"/>
          <stop offset="1" stop-color="var(--band-blue)"/>
        </linearGradient>
      </defs>
      <rect x="0" y="0" width="330" height="26" fill="url(#rearBlue)"/>
      <polygon points="0,300 330,300 330,348 165,395 0,348" fill="url(#rearBlue)"/>
      <polygon points="0,26 330,26 330,322 165,368 0,322" fill="url(#rearDark)"/>
    </svg>
    <div class="card-content promo">
      <p class="promo-tagline">SERVICE WHEN<br>YOU NEED IT!</p>
      <p class="promo-call">CALL NOW FOR OUR</p>
      <p class="promo-hours">24/7</p>
      <p class="promo-service">BREAKDOWN<br>SERVICE</p>
    </div>
    <div class="brand">
      <span class="brand-dot"></span>
      <span class="brand-name">BRIGHTWIRE POWER</span>
    </div>
  </section>

  <!-- Front side -->
  <section class="card card-front">
    <svg class="card-shape" viewBox="0 0 330 540" aria-hidden="true">
      <defs>
        <linearGradient id="frontDark" x1="0" y1="0" x2="0" y2="1">
          <stop offset="0" stop-color="var(--panel-dark-top)"/>
          <stop offset="0.35" stop-color="var(--panel-dark-mid)"/>
          <stop offset="1" stop-color="var(--panel-dark-bottom)"/>
        </linearGradient>
        <linearGradient id="frontBlue" x1="0" y1="0" x2="1" y2="0">
          <stop offset="0" stop-color="var(--band-blue-deep)"/>
          <stop offset="0.5" stop-color="var(--band-blue-light)"/>
          <stop offset="1" stop-color="var(--band-blue)"/>
        </linearGradient>
      </defs>
      <rect x="0" y="0" width="330" height="26" fill="url(#frontBlue)"/>
      <polygon points="0,300 330,300 330,348 165,395 0,348" fill="url(#frontBlue)"/>
      <polygon points="0,26 330,26 330,322 165,368 0,322" fill="url(#frontDark)"/>
    </svg>
    <div class="card-content contact">
      <h1 class="contact-name">Marcus Penhale</h1>
      <p class="contact-role">Electrical Contractor</p>
      <ul class="contact-list">
        <li class="contact-item">
          <svg class="contact-icon" viewBox="0 0 20 20" aria-label="Telephone"><circle cx="10" cy="10" r="10" fill="#fff"/><path d="M6 5.5c.6-.6 1.3-.5 1.7.1l1 1.5c.3.5.2 1-.2 1.3l-.6.5c.6 1.3 1.6 2.3 2.9 2.9l.5-.6c.3-.4.8-.5 1.3-.2l1.5 1c.6.4.7 1.1.1 1.7-2.2 2.2-10.4-6-8.2-8.2z" fill="var(--icon-dark)"/></svg>
          (08) 8456 3071
        </li>
        <li class="contact-item">
          <svg class="contact-icon" viewBox="0 0 20 20" aria-label="Fax"><circle cx="10" cy="10" r="10" fill="#fff"/><rect x="7" y="4.5" width="6" height="4" fill="var(--icon-dark)"/><rect x="5" y="8.5" width="10" height="5" rx="1" fill="var(--icon-dark)"/><rect x="7" y="12" width="6" height="3.5" fill="var(--icon-dark)"/></svg>
          (08) 8679 4315
        </li>
        <li class="contact-item">
          <svg class="contact-icon" viewBox="0 0 20 20" aria-label="Mobile"><circle cx="10" cy="10" r="10" fill="#fff"/><rect x="7" y="4" width="6" height="12" rx="1.2" fill="var(--icon-dark)"/><rect x="8" y="5.5" width="4" height="6" fill="#fff"/></svg>
          0438 562 740
        </li>
        <li class="contact-item small">
          <svg class="contact-icon" viewBox="0 0 20 20" aria-label="Email"><circle cx="10" cy="10" r="10" fill="#fff"/><rect x="4.5" y="6.5" width="11" height="7.5" fill="var(--icon-dark)"/><path d="M4.5 6.5l5.5 4.2 5.5-4.2" fill="none" stroke="#fff" stroke-width="1"/></svg>
          marcus.penhale@brightwirepower.com.au
        </li>
        <li class="contact-item small">
          <svg class="contact-icon" viewBox="0 0 20 20" aria-label="Website"><circle cx="10" cy="10" r="10" fill="#fff"/><rect x="4.5" y="5.5" width="11" height="7.5" rx="0.8" fill="var(--icon-dark)"/><rect x="8.5" y="13" width="3" height="1.5" fill="var(--icon-dark)"/><rect x="6.5" y="14.5" width="7" height="1" fill="var(--icon-dark)"/></svg>
          www.brightwirepower.com.au
        </li>
      </ul>
      <p class="contact-tagline">SERVICE<br>WHEN YOU NEED IT</p>
    </div>
    <div class="brand">
      <span class="brand-dot"></span>
      <span class="brand-name">BRIGHTWIRE POWER</span>
    </div>
  </section>

</main>
</body>
</html>
```